Medspa business needs a webpage

we need a website for a new Medspa company based in Lynden, WA called Lumara Vale Medical Aesthetics. We offer non surgical, cosmetic procedures as well as medical weight loss. We would like a sleek design, with rich colors (dark, emerald green and gold). The website should list our services, pricing and links to book appointments.

```html
<!DOCTYPE html>
<html lang="en">
<head>
<meta charset="utf-8">
<title>Lumara Vale Medical Aesthetics</title>
<link href="https://fonts.googleapis.com/css2?family=Playfair+Display:wght@600;700&family=Inter:wght@400;500;600&display=swap" rel="stylesheet">
<style>
:root{
  --mat:#6b6b6b;
  --bg:#0e1d18;
  --band:#12241e;
  --card:#10201b;
  --line:#26392f;
  --gold:#c4a76a;
  --gold-text:#d9bb72;
  --ink:#ffffff;
  --muted:#dfe5e1;
  --dark:#0d1a14;
}
*{box-sizing:border-box;margin:0;padding:0}
html,body{width:1200px;height:2282px;overflow:hidden;background:var(--mat)}
body{font-family:"Inter",sans-serif;color:var(--ink);position:relative}
.page{position:absolute;left:81px;top:81px;width:1038px;height:2119px;background:var(--bg);box-shadow:0 10px 30px rgba(0,0,0,.35);overflow:hidden}
.serif{font-family:"Playfair Display",serif}
.header{position:absolute;left:0;top:0;width:100%;height:37px;background:var(--gold);z-index:3}
.brand{position:absolute;left:60px;top:0;width:94px;height:80px;background:var(--dark);display:flex;align-items:center;justify-content:center;text-align:center;font-size:10px;letter-spacing:2px;color:var(--gold);font-weight:500;line-height:1.5;z-index:4}
.nav{position:absolute;right:60px;top:0;height:37px;display:flex;align-items:center;gap:23px;font-size:10px;font-weight:500;color:#14201a}
.btn{display:inline-flex;align-items:center;justify-content:center;border-radius:14px;font-weight:600;white-space:nowrap}
.nav .btn{background:#0f2a1c;color:var(--gold-text);height:26px;padding:0 11px;margin-left:-2px}
.hero{position:absolute;left:0;top:37px;width:100%;height:470px;background:linear-gradient(90deg,#1c2a1d 0%,#0f1f1a 30%,#0f1f1a 100%)}
.hero-photo{position:absolute;left:388px;top:0;right:0;bottom:0;background:radial-gradient(ellipse at 50% 45%,#e4c1a7 0%,#c99f84 28%,#e9e9ee 52%,#0f1f1a 78%)}
.hero-copy{position:absolute;left:71px;top:145px;width:320px}
.eyebrow{color:var(--gold);font-size:16px;font-weight:600;display:flex;align-items:center;gap:3px}
.eyebrow span{width:30px;height:1.5px;background:var(--gold);margin-top:9px}
.hero h1{font-size:44px;line-height:1.15;margin-top:10px;font-weight:700}
.hero p{font-size:16px;line-height:1.45;margin-top:11px}
.hero-actions{margin-top:14px;display:flex;gap:6px}
.hero-actions .btn{height:24px;padding:0 12px;font-size:10px}
.btn-light{background:#fff;color:#111}
.btn-gold{background:var(--gold);color:#15201a}
.trust{position:absolute;left:0;top:507px;width:100%;height:47px;background:var(--band);border-bottom:1px solid var(--line);display:flex;justify-content:center;align-items:center;gap:5px}
.pill{width:195px;height:28px;border:1px solid var(--line);border-radius:14px;font-size:8.5px;font-weight:600;display:flex;align-items:center;justify-content:center}
.section{position:absolute;left:0;width:100%}
.wrap{position:absolute;left:221px;width:595px}
.title{font-family:"Playfair Display",serif;font-weight:600;font-size:20px;position:relative;padding-left:10px}
.title::before{content:"";position:absolute;left:0;top:1px;width:4px;height:4px;background:var(--gold)}
.card{background:var(--card);border:1px solid var(--line);border-radius:6px;padding:10px}
.card h3{font-family:"Playfair Display",serif;font-size:11.5px;font-weight:600}
.card p{font-size:8.6px;line-height:1.6;margin-top:8px;color:var(--muted)}
.card ul{list-style:none;margin-top:8px}
.card li{font-size:8.6px;line-height:1.55;margin-bottom:2.5px;padding-left:9px;position:relative;color:var(--muted)}
.card li::before{content:"•";position:absolute;left:0}
.link{color:var(--gold-text);font-size:8.6px;font-weight:600;margin-top:5px;display:block}
.services{top:554px;height:275px}
.grid3{display:grid;grid-template-columns:repeat(3,190px);gap:12px;margin-top:13px}
.grid3 .card{height:165px}
.pricing{top:829px;height:312px;background:var(--band)}
.grid4{display:grid;grid-template-columns:repeat(4,139px);gap:13px;margin-top:13px}
.grid4 .card{height:178px}
.price{font-family:"Playfair Display",serif;font-size:16px;margin-top:9px}
.price small{font-family:"Inter",sans-serif;font-size:7.5px;color:var(--muted)}
.grid4 ul{margin-top:6px}
.card .btn{background:var(--gold);color:#15201a;height:22px;padding:0 9px;font-size:8px;margin-top:3px}
.note{font-size:7px;color:#c3cbc6;margin-top:11px}
.providers{top:1141px;height:446px}
.pcard{position:absolute;top:87px;width:247px;height:315px;padding:10px}
.photo{width:227px;height:227px;border-radius:4px}
.pcard h3{margin-top:9px;font-size:11.5px}
.pcard p{margin-top:9px}
.cta{top:1587px;height:133px;background:var(--band);border-top:1px solid var(--line);border-bottom:1px solid var(--line)}
.cta h2{font-family:"Playfair Display",serif;font-size:20px;font-weight:600}
.cta p{font-size:8.6px;margin-top:10px}
.cta-actions{position:absolute;right:0;top:-3px;display:flex;gap:7px}
.cta-actions .btn{height:27px;padding:0 10px;font-size:9px}
.btn-outline{border:1px solid var(--gold);color:var(--gold-text)}
.visit{top:1720px;height:346px}
.visit address{font-style:normal;font-size:8.6px;margin-top:22px}
.visit .link{margin-top:14px}
.contact-list{list-style:none;margin:14px 0 0 14px}
.contact-list li{font-size:8.6px;color:var(--gold-text);font-weight:600;line-height:1.6}
.contact-list li::before{content:"• ";color:#fff}
.form{position:absolute;left:332px;top:35px;width:263px;height:276px;padding:14px 10px}
.form label{display:block;font-size:8.6px;margin-bottom:5px}
.field{height:22px;border:1px solid var(--line);border-radius:5px;background:#0b1813;font-size:6.8px;color:#9aa49f;padding:0 8px;display:flex;align-items:center;margin-bottom:10px}
.field.select{color:#fff;justify-content:space-between}
.field.area{height:46px;align-items:flex-start;padding-top:8px;font-family:monospace}
.send{height:20px;border-radius:10px;background:var(--gold);color:#15201a;font-size:7px;font-weight:600;display:flex;align-items:center;justify-content:center;margin-top:-4px}
.form small{display:block;font-size:7px;color:#c3cbc6;margin-top:10px}
.footer{top:2066px;height:53px;background:#0c1915;border-top:1px solid var(--line)}
.footer .wrap{top:21px;display:flex;justify-content:space-between;font-size:8.6px}
.footer nav{display:flex;gap:9px}
</style>
</head>
<body>
<div class="page">
  <header class="header">
    <nav class="nav"><span>Home</span><span>Services</span><span>Pricing</span><span>Team</span><span>Contact</span><span class="btn">Book Now</span></nav>
  </header>
  <div class="brand">LUMARA<br>VALE</div>

  <section class="hero">
    <div class="hero-photo" role="img" aria-label="Portrait of a client receiving a facial assessment from a gloved provider"></div>
    <div class="hero-copy">
      <div class="eyebrow">ELEVATE YOUR SKIN.<span></span></div>
      <h1 class="serif">Enhance Your Confidence.</h1>
      <p>Non-surgical aesthetic treatments and medical weight loss in Lynden, WA.</p>
      <div class="hero-actions"><span class="btn btn-light">Book an Appointment</span><span class="btn btn-gold">Explore Services</span></div>
    </div>
  </section>

  <div class="trust"><div class="pill">Board-Certified Providers</div><div class="pill">Medical-Grade Treatments</div><div class="pill">Personalized Care Plans</div></div>

  <section class="section services">
    <div class="wrap" style="top:40px">
      <h2 class="title">Our Services</h2>
      <div class="grid3">
        <div class="card"><h3>Injectables</h3><p>Neuromodulators and dermal fillers to smooth lines, restore volume, and refine contours.</p><ul><li>Wrinkle Relaxers</li><li>Lip &amp; Cheek Filler</li><li>Jawline &amp; Chin Contour</li></ul><span class="link">Book injectables →</span></div>
        <div class="card"><h3>Skin Rejuvenation</h3><p>Treat texture, tone, and radiance with non-invasive solutions and minimal downtime.</p><ul><li>Microneedling</li><li>Medical-grade Peels</li><li>LED &amp; Collagen Therapy</li></ul><span class="link">Book skin rejuvenation →</span></div>
        <div class="card"><h3>Medical Weight Loss</h3><p>Clinically guided programs tailored to your goals with ongoing provider support.</p><ul><li>Consultation &amp; Labs</li><li>GLP-1 Assisted Plans</li><li>Nutrition &amp; Coaching</li></ul><span class="link">Book weight loss consult →</span></div>
      </div>
    </div>
  </section>

  <section class="section pricing">
    <div class="wrap" style="top:42px">
      <h2 class="title">Transparent Pricing</h2>
      <div class="grid4">
        <div class="card"><h3>Neuromodulators</h3><div class="price">$12–$14 <small>/unit</small></div><ul><li>Forehead, Glabella, Crow's Feet</li><li>Treatment plan review</li><li>Follow-up tweak within 2 weeks</li></ul><span class="btn">Book</span></div>
        <div class="card"><h3>Dermal Fillers</h3><div class="price">$650–$800 <small>/syringe</small></div><ul><li>Lips, Cheeks, Jawline, Chin</li><li>Includes numbing &amp; aftercare</li><li>1:1 aesthetic mapping</li></ul><span class="btn">Book</span></div>
        <div class="card"><h3>Microneedling</h3><div class="price">$299 <small>/session</small></div><ul><li>Face &amp; Neck</li><li>Medical-grade serums</li><li>Series packages available</li></ul><span class="btn">Book</span></div>
        <div class="card"><h3>Weight Loss Program</h3><div class="price">$249 <small>/month</small></div><ul><li>Provider consult &amp; labs</li><li>Medication when appropriate</li><li>Coaching &amp; check-ins</li></ul><span class="btn">Start Now</span></div>
      </div>
      <p class="note">* Pricing shown for contest demo. Final quotes provided after consultation.</p>
    </div>
  </section>

  <section class="section providers">
    <div class="wrap" style="top:44px;height:402px">
      <h2 class="title">Meet Your Providers</h2>
      <div class="card pcard" style="left:23px;top:44px"><div class="photo" role="img" aria-label="Headshot of Nadia Rowe, ARNP" style="background:linear-gradient(160deg,#8c979c,#5d676b 60%,#2a2d2f)"></div><h3>Nadia Rowe, ARNP</h3><p>Board-certified nurse practitioner specializing in injectables and regenerative skin health.</p></div>
      <div class="card pcard" style="left:326px;top:44px"><div class="photo" role="img" aria-label="Headshot of Elena Marsh, PA-C" style="background:linear-gradient(160deg,#a7adb0,#7d8386 60%,#2c2d2e)"></div><h3>Elena Marsh, PA-C</h3><p>Physician associate focused on dermatology, laser-free rejuvenation, and patient education.</p></div>
    </div>
  </section>

  <section class="section cta">
    <div class="wrap" style="top:40px">
      <h2>Ready to glow?</h2>
      <p>Reserve your appointment in minutes. New patients welcome.</p>
      <div class="cta-actions"><span class="btn btn-gold">Book Online</span><span class="btn btn-outline">Call (360) 555-0187</span></div>
    </div>
  </section>

  <section class="section visit">
    <div class="wrap" style="top:42px;height:300px">
      <h2 class="title">Visit Us</h2>
      <address>418 Cedar Grove Ave, Lynden, WA 98264</address>
      <span class="link">Get directions →</span>
      <ul class="contact-list"><li>Call: (360) 555-0187</li><li>Email: hello@lumaravale.com</li><li>Book online</li></ul>
      <div class="card form" style="top:-8px">
        <label>Name</label><div class="field">Your full name</div>
        <label>Email</label><div class="field">you@example.com</div>
        <label>Service</label><div class="field select"><span>Injectables</span><span>⌄</span></div>
        <label>Message</label><div class="field area">Tell us your goals</div>
        <div class="send">Send Message</div>
        <small>Demo form for contest—replace with platform form or CRM embed.</small>
      </div>
    </div>
  </section>

  <footer class="section footer">
    <div class="wrap"><span>© 2025 Lumara Vale Medical Aesthetics • Lynden, WA</span><nav><span>Services</span><span>Pricing</span><span>Book</span><span>Privacy</span></nav></div>
  </footer>
</div>
</body>
</html>
```